Fahrzeugbeschriftung für ambulanten Pflegedienst
Zielgruppe
Ambulanter Pflegedienst
(Bitte um deutsche Kommunikation)
Aufgabenstellung
Unser Logo und unser Motto, farbliche Komponenten, die wichtigste Leistungen, Mail Adresse, Flyer vorhanden, Fahrzeuge haben einen weißen Hintergrund. Es sind 3 Fahrzeug Modelle : Zipo Kleinflink Baujahr 2008, Norvak Reihe 5 Baujahr 2023 und KR Ilo 2 Türig Baujahr 2008, Kontaktdaten wie Telefonnummer und Mail Adresse müssen sichtlich sein.
Die Welle im Flyer soll auch auf den Fahrzeugen abgebildet sein.
Hierbei stellen wir uns folgendes vor:
Die zweifarbige Teilung, mit der Welle, soll sich von A - Säule bis C-Säule vollstrecken.
Abbildungen vom Flyer soll genutzt werden, z.B. Die Hand mit den Personen.
Ein Beispiel, für Auffälligkeit habe ich 3 Bilder von anderen Fahrzeugen beigefügt (nur als Beispiel)
Die Schrift 'Ambulanter Pflegedienst' muss betont sein.
Zu unseren Leistungen die aufgeführt werden müssen;
- Grundpflege
- Behandlungspflege
- Wundmanagement
- Pflegeberatung

```html
<!DOCTYPE html>
<html lang="de">
<head>
<meta charset="utf-8">
<title>SorgSam – Fahrzeugbeschriftung</title>
<link rel="stylesheet" href="https://fonts.googleapis.com/css2?family=Signika:wght@600&family=Questrial&family=Montserrat:wght@500&display=swap">
<style>
  :root {
    --teal: #6aa9c0;
    --ink: #5b6066;
    --paper: #ffffff;
    --body-line: #c9ced3;
    --glass: #3b3f43;
    --tyre: #26282b;
    --rim: #a3a9ae;
    --stripe: #1d1f22;
    --art-a: #f2b8a6;
    --art-b: #4d9a8a;
  }
  * { margin: 0; padding: 0; box-sizing: border-box; }
  html, body { width: 936px; height: 1200px; overflow: hidden; background: var(--paper); }
  .canvas { position: relative; width: 936px; height: 1200px; }
  .vehicles { position: absolute; inset: 0; }
  .abs { position: absolute; white-space: nowrap; }
  .contact { font-family: "Montserrat", sans-serif; font-weight: 500; color: var(--teal); display: flex; align-items: center; gap: 4px; line-height: 1; }
  .contact svg { fill: var(--teal); flex: none; }
  .contact .sep { margin: 0 3px; }
  .brand { font-family: "Signika", sans-serif; font-weight: 600; color: var(--ink); line-height: 1; }
  .rule { height: 1.5px; background: var(--teal); }
  .claim { font-family: "Questrial", sans-serif; color: var(--ink); line-height: 1; }
  .services { font-family: "Montserrat", sans-serif; font-weight: 500; color: #33373b; line-height: 1.4; }
  .care-art { position: absolute; border-radius: 45% 45% 40% 40%;
    background: linear-gradient(165deg, var(--art-b) 0%, #7fb7a9 45%, var(--art-a) 100%); }
</style>
</head>
<body>
<div class="canvas">
  <svg class="vehicles" width="936" height="1200" viewBox="0 0 936 1200" aria-hidden="true">
    <defs>
      <clipPath id="hatch-body"><path d="M100,305 L92,250 Q95,160 130,110 L150,60 Q160,46 200,44 L520,41 Q562,42 602,66 L682,130 Q772,150 812,186 Q832,212 830,262 L828,305 Z"/></clipPath>
      <clipPath id="sedan-body"><path d="M35,700 Q28,640 40,560 L50,545 Q120,520 170,495 Q260,462 360,460 Q480,462 560,500 L650,555 Q800,570 880,590 Q915,610 918,650 L915,700 Q900,712 860,712 L80,712 Z"/></clipPath>
      <clipPath id="city-body"><path d="M168,1085 Q160,1010 185,960 L215,850 Q225,832 260,830 L400,827 Q440,830 470,850 L560,935 Q640,955 655,990 L665,1060 L660,1090 Z"/></clipPath>
    </defs>

    <!-- two-door hatch -->
    <path d="M100,305 L92,250 Q95,160 130,110 L150,60 Q160,46 200,44 L520,41 Q562,42 602,66 L682,130 Q772,150 812,186 Q832,212 830,262 L828,305 Z" fill="var(--paper)" stroke="var(--body-line)" stroke-width="2"/>
    <g clip-path="url(#hatch-body)">
      <polygon points="310,30 384,30 316,316 261,316" fill="var(--teal)"/>
      <rect x="263" y="280" width="377" height="4" fill="var(--stripe)"/>
      <rect x="263" y="287" width="377" height="2" fill="var(--stripe)"/>
    </g>
    <path d="M200,70 L340,63 L560,62 Q600,66 650,135 L650,158 L340,158 L205,118 Q190,95 200,70 Z" fill="var(--glass)"/>
    <circle cx="302" cy="220" r="22" fill="none" stroke="var(--paper)" stroke-width="3"/>
    <circle cx="189" cy="300" r="57" fill="var(--tyre)"/><circle cx="189" cy="300" r="40" fill="var(--rim)"/><circle cx="189" cy="300" r="10" fill="var(--tyre)"/>
    <circle cx="713" cy="300" r="57" fill="var(--tyre)"/><circle cx="713" cy="300" r="40" fill="var(--rim)"/><circle cx="713" cy="300" r="10" fill="var(--tyre)"/>

    <!-- sedan -->
    <path d="M35,700 Q28,640 40,560 L50,545 Q120,520 170,495 Q260,462 360,460 Q480,462 560,500 L650,555 Q800,570 880,590 Q915,610 918,650 L915,700 Q900,712 860,712 L80,712 Z" fill="var(--paper)" stroke="var(--body-line)" stroke-width="2"/>
    <g clip-path="url(#sedan-body)">
      <polygon points="349,455 425,455 365,712 290,712" fill="var(--teal)"/>
    </g>
    <path d="M165,505 Q260,476 370,474 Q470,476 540,506 L610,548 L170,548 Z" fill="var(--glass)"/>
    <circle cx="352" cy="619" r="22" fill="none" stroke="var(--paper)" stroke-width="3"/>
    <circle cx="189" cy="669" r="62" fill="var(--tyre)"/><circle cx="189" cy="669" r="44" fill="#3d4044"/><circle cx="189" cy="669" r="8" fill="var(--rim)"/>
    <circle cx="772" cy="669" r="62" fill="var(--tyre)"/><circle cx="772" cy="669" r="44" fill="#3d4044"/><circle cx="772" cy="669" r="8" fill="var(--rim)"/>

    <!-- city car -->
    <path d="M168,1085 Q160,1010 185,960 L215,850 Q225,832 260,830 L400,827 Q440,830 470,850 L560,935 Q640,955 655,990 L665,1060 L660,1090 Z" fill="var(--paper)" stroke="var(--body-line)" stroke-width="2"/>
    <g clip-path="url(#city-body)">
      <polygon points="337,820 399,820 335,1092 302,1092" fill="var(--teal)"/>
    </g>
    <path d="M290,850 L395,845 Q430,848 460,870 L530,933 L290,933 Z" fill="var(--glass)"/>
    <path d="M228,850 L270,848 L270,925 L205,925 Z" fill="var(--glass)"/>
    <circle cx="338" cy="981" r="19" fill="none" stroke="var(--paper)" stroke-width="3"/>
    <circle cx="234" cy="1080" r="52" fill="var(--tyre)"/><circle cx="234" cy="1080" r="36" fill="var(--rim)"/><circle cx="234" cy="1080" r="8" fill="var(--tyre)"/>
    <circle cx="591" cy="1080" r="52" fill="var(--tyre)"/><circle cx="591" cy="1080" r="36" fill="var(--rim)"/><circle cx="591" cy="1080" r="8" fill="var(--tyre)"/>
  </svg>

  <!-- hatch -->
  <div class="care-art" role="img" aria-label="Illustration: Hand mit Pflegekraft und Person im Rollstuhl" style="left:144px;top:154px;width:82px;height:72px"></div>
  <div class="abs contact" style="left:402px;top:178px;font-size:10.5px">
    <svg width="10" height="10" viewBox="0 0 24 24"><path d="M6.6 10.8a15.1 15.1 0 0 0 6.6 6.6l2.2-2.2c.3-.3.7-.4 1-.2 1.1.4 2.3.6 3.6.6.6 0 1 .4 1 1V20c0 .6-.4 1-1 1A17 17 0 0 1 3 4c0-.6.4-1 1-1h3.5c.6 0 1 .4 1 1 0 1.3.2 2.5.6 3.6.1.3 0 .7-.2 1z"/></svg>06201 48 27 310<span class="sep">·</span>
    <svg width="11" height="9" viewBox="0 0 24 18"><path d="M0 0h24v18H0zM2 2v.6l10 7 10-7V2zm0 3v11h20V5l-10 7z"/></svg>info@sorgsam-pflege.de</div>
  <div class="abs brand" style="left:345px;top:192px;font-size:40px">SorgSam</div>
  <div class="abs rule" style="left:345px;top:233px;width:248px"></div>
  <div class="abs claim" style="left:345px;top:237px;font-size:17.5px;letter-spacing:0.09em">Ambulanter Pflegedienst</div>
  <div class="abs services" style="left:345px;top:257px;font-size:7.5px">Pflegeberatung · Grund, -Behandlungspflege · Wundmanagement</div>

  <!-- sedan -->
  <div class="care-art" role="img" aria-label="Illustration: Hand mit Pflegekraft und Person im Rollstuhl" style="left:103px;top:525px;width:86px;height:76px"></div>
  <div class="abs contact" style="left:456px;top:577px;font-size:10.5px">
    <svg width="10" height="10" viewBox="0 0 24 24"><path d="M6.6 10.8a15.1 15.1 0 0 0 6.6 6.6l2.2-2.2c.3-.3.7-.4 1-.2 1.1.4 2.3.6 3.6.6.6 0 1 .4 1 1V20c0 .6-.4 1-1 1A17 17 0 0 1 3 4c0-.6.4-1 1-1h3.5c.6 0 1 .4 1 1 0 1.3.2 2.5.6 3.6.1.3 0 .7-.2 1z"/></svg>06201 48 27 310<span class="sep">·</span>
    <svg width="11" height="9" viewBox="0 0 24 18"><path d="M0 0h24v18H0zM2 2v.6l10 7 10-7V2zm0 3v11h20V5l-10 7z"/></svg>info@sorgsam-pflege.de</div>
  <div class="abs brand" style="left:400px;top:591px;font-size:40px">SorgSam</div>
  <div class="abs rule" style="left:400px;top:632px;width:247px"></div>
  <div class="abs claim" style="left:400px;top:636px;font-size:17.5px;letter-spacing:0.09em">Ambulanter Pflegedienst</div>
  <div class="abs services" style="left:400px;top:656px;font-size:7.5px">Pflegeberatung · Grund, -Behandlungspflege · Wundmanagement</div>

  <!-- city car -->
  <div class="care-art" role="img" aria-label="Illustration: Hand mit Pflegekraft und Person im Rollstuhl" style="left:201px;top:944px;width:82px;height:80px"></div>
  <div class="abs contact" style="left:376px;top:945px;font-size:8.5px">
    <svg width="8" height="8" viewBox="0 0 24 24"><path d="M6.6 10.8a15.1 15.1 0 0 0 6.6 6.6l2.2-2.2c.3-.3.7-.4 1-.2 1.1.4 2.3.6 3.6.6.6 0 1 .4 1 1V20c0 .6-.4 1-1 1A17 17 0 0 1 3 4c0-.6.4-1 1-1h3.5c.6 0 1 .4 1 1 0 1.3.2 2.5.6 3.6.1.3 0 .7-.2 1z"/></svg>06201 48 27 310<span class="sep">·</span>
    <svg width="9" height="7" viewBox="0 0 24 18"><path d="M0 0h24v18H0zM2 2v.6l10 7 10-7V2zm0 3v11h20V5l-10 7z"/></svg>info@sorgsam-pflege.de</div>
  <div class="abs brand" style="left:375px;top:957px;font-size:33px">SorgSam</div>
  <div class="abs rule" style="left:375px;top:991px;width:197px"></div>
  <div class="abs claim" style="left:375px;top:995px;font-size:14px;letter-spacing:0.09em">Ambulanter Pflegedienst</div>
  <div class="abs services" style="left:375px;top:1012px;font-size:8px">Pflegeberatung<br>Grund, -Behandlungspflege<br>Wundmanagement</div>
</div>
</body>
</html>
```